Business Card Design Project - 2 sided

We need a business card design for a card having one business on each side (ie. two businesses on one card). Would like a design that incorporates logo, tagline and normal fields (name, position, address, phone).

Would also like an allowance for small font text along the bottom (text to be determined, but less than 50 characters).

NB. Attached logo for Verbica Partners has two variations - either can be used.

www.verbicapartners.com / www.kelvarho.com

```html
<!DOCTYPE html>
<html lang="en">
<head>
<meta charset="utf-8">
<title>Verbica Partners / Kelvarho – Two-Sided Business Card</title>
<link rel="stylesheet" href="https://fonts.googleapis.com/css2?family=Open+Sans:ital,wght@0,400;0,600;0,700;1,400&display=swap">
<style>
  :root {
    --navy: #27237a;
    --green: #7dc242;
    --rule: #c9c9cf;
    --divider: #e4e4ea;
    --ink: #1e1e1e;
    --paper: #ffffff;
    --backdrop: #e6e3df;
    --card-w: 700px;
    --card-h: 400px;
  }
  * { box-sizing: border-box; margin: 0; padding: 0; }
  html, body {
    width: 1200px; height: 900px; overflow: hidden;
    background: var(--backdrop);
    font-family: "Open Sans", Arial, sans-serif;
  }
  .sheet {
    width: 1200px; height: 900px;
    display: flex; flex-direction: column; align-items: center; justify-content: center;
    gap: 40px;
  }
  .card {
    position: relative;
    width: var(--card-w); height: var(--card-h);
    background: var(--paper);
    overflow: hidden;
    box-shadow: 0 6px 18px rgba(0,0,0,.18);
  }
  .card__art { position: absolute; inset: 0; }

  .brand { display: flex; align-items: center; gap: 12px; }
  .brand-dot { border-radius: 50%; background: var(--green); flex: none; }
  .brand-name { color: var(--navy); font-weight: 700; white-space: nowrap; }

  /* Front – Verbica Partners */
  .front__brand { position: absolute; left: 70px; top: 118px; }
  .front__brand .brand-dot { width: 22px; height: 22px; }
  .front__brand .brand-name { font-size: 40px; letter-spacing: .5px; }
  .front__tagline {
    position: absolute; left: 106px; top: 180px;
    font-size: 16px; font-style: italic; color: var(--navy);
  }
  .front__web {
    position: absolute; left: 330px; top: 292px;
    font-size: 22px; font-weight: 700; color: var(--paper);
    transform: rotate(-13deg); transform-origin: left center;
  }

  /* Back – Kelvarho */
  .back__brand { position: absolute; left: 60px; top: 170px; }
  .back__brand .brand-dot { width: 18px; height: 18px; }
  .back__brand .brand-name { font-size: 34px; font-weight: 600; }
  .back__details { position: absolute; left: 365px; top: 62px; }
  .person-name { font-size: 32px; color: var(--ink); line-height: 1.1; }
  .person-title { font-size: 21px; color: var(--green); margin-bottom: 18px; }
  .contact-list { list-style: none; }
  .contact-list li {
    display: flex; align-items: center; gap: 12px;
    font-size: 16px; color: var(--ink); line-height: 1.6;
  }
  .contact-list svg { width: 16px; height: 16px; flex: none; }
  .back__footnote {
    position: absolute; right: 24px; bottom: 12px;
    font-size: 12px; color: var(--paper); letter-spacing: .3px;
  }
</style>
</head>
<body>
<main class="sheet">

  <section class="card card--front" aria-label="Card front: Verbica Partners">
    <svg class="card__art" viewBox="0 0 700 400" aria-hidden="true">
      <path d="M0,322 C220,292 460,245 700,128" fill="none" stroke="var(--rule)" stroke-width="5"/>
      <path d="M0,334 C220,304 460,258 700,140 L700,400 L0,400 Z" fill="var(--navy)"/>
    </svg>
    <div class="brand front__brand">
      <span class="brand-dot"></span>
      <span class="brand-name">Verbica Partners</span>
    </div>
    <p class="front__tagline">Website Translation and Localisation Specialist....</p>
    <p class="front__web">www.verbicapartners.com</p>
  </section>

  <section class="card card--back" aria-label="Card back: Kelvarho">
    <svg class="card__art" viewBox="0 0 700 400" aria-hidden="true">
      <line x1="335" y1="40" x2="335" y2="300" stroke="var(--divider)" stroke-width="2"/>
      <path d="M0,360 L322,360 L306,400 L0,400 Z" fill="var(--green)"/>
      <path d="M322,360 L700,322 L700,400 L306,400 Z" fill="var(--navy)"/>
    </svg>
    <div class="brand back__brand">
      <span class="brand-dot"></span>
      <span class="brand-name">Kelvarho</span>
    </div>
    <div class="back__details">
      <p class="person-name">Mara Ellison</p>
      <p class="person-title">Title here</p>
      <ul class="contact-list">
        <li>
          <svg viewBox="0 0 16 16" aria-hidden="true"><path d="M8 1a5 5 0 0 1 5 5c0 4-5 9-5 9S3 10 3 6a5 5 0 0 1 5-5z" fill="var(--green)"/><circle cx="8" cy="6" r="2" fill="#fff"/></svg>
          Street Address here
        </li>
        <li>
          <svg viewBox="0 0 16 16" aria-hidden="true"><path d="M4 1l3 3-2 2c1 2 3 4 5 5l2-2 3 3-2 3C7 15 1 9 1 3z" fill="var(--green)"/></svg>
          (123) 456 7890
        </li>
        <li>
          <svg viewBox="0 0 16 16" aria-hidden="true"><rect x="4" y="1" width="8" height="5" fill="var(--green)"/><rect x="1" y="6" width="14" height="7" rx="1" fill="var(--green)"/><rect x="4" y="10" width="8" height="5" fill="#fff" stroke="var(--green)"/></svg>
          (123) 456 7890
        </li>
        <li>
          <svg viewBox="0 0 16 16" aria-hidden="true"><rect x="1" y="3" width="14" height="10" rx="1" fill="var(--green)"/><path d="M1 4l7 5 7-5" fill="none" stroke="#fff" stroke-width="1.4"/></svg>
          info@kelvarho.com
        </li>
      </ul>
    </div>
    <p class="back__footnote">www.kelvarho.com · Translation made simple</p>
  </section>

</main>
</body>
</html>
```